Business Card Design Project

Business Card
We are rebranding with a new logo
Industry/Entity Type
Business
Contact Information for Business Card
Dennis Marlow +61 427581962 dennis@qovo.com.au P.O. Box 872 Kelvindale QLD 4309
Requirements
Must have
- Logo

```html
<!DOCTYPE html>
<html lang="en">
<head>
<meta charset="utf-8">
<title>Qovo International – Business Card</title>
<link rel="stylesheet" href="https://fonts.googleapis.com/css2?family=Roboto:wght@400;500&family=Roboto+Condensed:wght@700&display=swap">
<style>
  :root {
    --backdrop: #2a2a2a;
    --card: #f2f2f2;
    --brand-blue: #1a8bc4;
    --band-blue-dark: #0d5f8f;
    --brand-orange: #f0851f;
    --text-grey: #4a4a4a;
    --divider: #c9c9c9;
    --band-text: #e6f3fa;
  }
  * { box-sizing: border-box; margin: 0; padding: 0; }
  html, body {
    width: 1200px;
    height: 960px;
    overflow: hidden;
    background: var(--backdrop);
  }
  .card {
    position: absolute;
    left: 223px;
    top: 265px;
    width: 754px;
    height: 432px;
    border-radius: 18px;
    background: var(--card);
    overflow: hidden;
    font-family: "Roboto", Arial, sans-serif;
  }
  .brand {
    position: absolute;
    left: 60px;
    top: 170px;
    width: 320px;
    display: flex;
    align-items: center;
    justify-content: center;
    gap: 10px;
  }
  .brand-dot {
    width: 14px;
    height: 14px;
    border-radius: 50%;
    background: var(--brand-orange);
  }
  .brand-name {
    font-family: "Roboto", Arial, sans-serif;
    font-weight: 500;
    font-size: 30px;
    color: var(--brand-blue);
    letter-spacing: 0.5px;
  }
  .divider {
    position: absolute;
    left: 396px;
    top: 110px;
    width: 2px;
    height: 186px;
    background: linear-gradient(to bottom, transparent, var(--divider) 20%, var(--divider) 80%, transparent);
  }
  .contact {
    position: absolute;
    left: 437px;
    top: 120px;
    color: var(--text-grey);
    font-size: 18px;
    line-height: 23px;
  }
  .contact-name {
    font-family: "Roboto Condensed", Arial, sans-serif;
    font-weight: 700;
    font-size: 26px;
    color: var(--brand-blue);
    line-height: 30px;
    margin-bottom: 26px;
  }
  .contact-address { margin-bottom: 12px; }
  .contact-line {
    display: flex;
    align-items: center;
    gap: 10px;
    margin-left: -1px;
  }
  .contact-line svg { width: 17px; height: 17px; flex: none; }
  .footer-band {
    position: absolute;
    left: 0;
    bottom: 0;
    width: 754px;
    height: 100px;
  }
  .website {
    position: absolute;
    left: 0;
    bottom: 14px;
    width: 754px;
    text-align: center;
    color: var(--band-text);
    font-size: 17px;
    letter-spacing: 6px;
  }
</style>
</head>
<body>
  <div class="card">
    <div class="brand">
      <span class="brand-dot"></span>
      <span class="brand-name">Qovo International</span>
    </div>

    <div class="divider"></div>

    <div class="contact">
      <div class="contact-name">DENNIS MARLOW</div>
      <div class="contact-address">P.O. Box 872<br>Kelvindale QLD 4309</div>
      <div class="contact-line">
        <svg viewBox="0 0 24 24" aria-hidden="true"><path fill="var(--brand-blue)" d="M6.6 10.8a15.1 15.1 0 0 0 6.6 6.6l2.2-2.2c.3-.3.7-.4 1-.2 1.1.4 2.3.6 3.6.6.6 0 1 .4 1 1V20c0 .6-.4 1-1 1A17 17 0 0 1 3 4c0-.6.4-1 1-1h3.5c.6 0 1 .4 1 1 0 1.3.2 2.5.6 3.6.1.3 0 .7-.2 1z"/></svg>
        <span>+61 427581962</span>
      </div>
      <div class="contact-line">
        <svg viewBox="0 0 24 24" aria-hidden="true"><rect x="2" y="5" width="20" height="14" rx="1.5" fill="var(--brand-blue)"/><path d="M3 6.5l9 6.5 9-6.5" fill="none" stroke="var(--card)" stroke-width="1.6"/></svg>
        <span>dennis@qovo.com.au</span>
      </div>
    </div>

    <svg class="footer-band" viewBox="0 0 754 100" aria-hidden="true">
      <defs>
        <linearGradient id="bandGradient" x1="0" y1="0" x2="1" y2="0">
          <stop offset="0" stop-color="var(--band-blue-dark)"/>
          <stop offset="0.5" stop-color="var(--brand-blue)"/>
          <stop offset="1" stop-color="var(--band-blue-dark)"/>
        </linearGradient>
      </defs>
      <path d="M0 88 Q377 -4 754 88 L754 100 L0 100 Z" fill="var(--brand-orange)"/>
      <path d="M0 93 Q377 4 754 93 L754 100 L0 100 Z" fill="url(#bandGradient)"/>
    </svg>
    <div class="website">www.qovo.com.au</div>
  </div>
</body>
</html>
```